Thornfield Visa Group Business Card

Boston based immigration and tax law firm.
Will serve wealthy individuals who wish to immigrate to the US.
Colors as in Logo, blue white.
Delivering sophisticated legal services.
Attached please see logo design from website.
Target Market(s)
non-US citizens
Industry/Entity Type
Legal
Contact Information for Business Card
Gerald T. Hensworth, Esq. LL.M, M.Sc., M.Fin
Thornfield Visa Group LLC
47 Kessel Ave., #218
Boston, MA 02134
Boston +1 617 555 0143
London +44 20 7946 0381
Sydney +61 2 5550 1296
www.thornfieldvisagroup.example
ghensworth@thornfieldvisagroup.example
United States Immigration and Tax Counsel

```html
<!DOCTYPE html>
<html lang="en">
<head>
<meta charset="utf-8">
<title>Thornfield Visa Group – Business Card</title>
<link href="https://fonts.googleapis.com/css2?family=Exo+2:wght@400;500;600&display=swap" rel="stylesheet">
<style>
  :root {
    --navy: #0b2560;
    --ink-blue: #3a3f8f;
    --sky: #4ab3d6;
    --paper: #ffffff;
    --text: #2b2b33;
    --stage: #e9eaee;
  }
  * { box-sizing: border-box; margin: 0; padding: 0; }
  html, body {
    width: 1200px; height: 903px; overflow: hidden;
    background: var(--stage);
    font-family: "Exo 2", "Segoe UI", sans-serif;
  }
  .sheet {
    width: 1200px; height: 903px;
    display: flex; flex-direction: column; align-items: center; justify-content: center;
    gap: 48px;
  }
  .card {
    position: relative;
    width: 660px; height: 377px;
    box-shadow: 0 6px 18px rgba(0,0,0,.12);
    overflow: hidden;
  }

  /* ---------- Front ---------- */
  .card--front { background: var(--paper); color: var(--text); }
  .accent-tab {
    position: absolute; left: 132px; top: 0;
    width: 92px; height: 30px; background: var(--sky);
  }
  .front-brand {
    position: absolute; left: 70px; top: 86px;
    display: flex; align-items: center; gap: 12px;
    color: var(--navy); font-weight: 600; font-size: 25px; letter-spacing: .2px;
    padding-bottom: 6px; border-bottom: 1.5px solid var(--navy);
  }
  .brand-square {
    width: 38px; height: 38px; border: 2px solid var(--sky); flex: none;
  }
  .name-band {
    position: absolute; right: 0; top: 152px;
    width: 300px; height: 40px; background: var(--navy);
  }
  .person {
    position: absolute; left: 355px; top: 202px;
  }
  .person__name {
    color: var(--ink-blue); font-size: 19px; font-weight: 500; letter-spacing: 2.5px;
  }
  .person__role { font-size: 14px; margin-top: 2px; letter-spacing: .5px; }
  .address {
    position: absolute; left: 70px; top: 200px;
    display: flex; gap: 10px; font-size: 13px; line-height: 1.45;
  }
  .contacts {
    position: absolute; left: 230px; top: 248px;
    list-style: none; font-size: 12.5px; line-height: 1;
  }
  .contacts li { display: flex; align-items: center; gap: 9px; height: 21px; }
  .icon { width: 13px; height: 13px; flex: none; }
  .icon path, .icon rect, .icon circle { fill: var(--ink-blue); }

  /* ---------- Back ---------- */
  .card--back { background: var(--navy); }
  .back-brand {
    position: absolute; left: 50%; top: 50%; transform: translate(-50%, -50%);
    display: flex; align-items: center; gap: 16px;
    color: var(--paper); font-weight: 600; font-size: 34px; letter-spacing: .3px;
    padding-bottom: 8px; border-bottom: 1.5px solid rgba(255,255,255,.7);
    white-space: nowrap;
  }
  .back-brand .brand-square { width: 50px; height: 50px; }
</style>
</head>
<body>
<main class="sheet">

  <section class="card card--back" aria-label="Card back">
    <div class="back-brand"><span class="brand-square"></span>Thornfield Visa Group</div>
  </section>

  <section class="card card--front" aria-label="Card front">
    <div class="accent-tab"></div>
    <div class="front-brand"><span class="brand-square"></span>Thornfield Visa Group</div>
    <div class="name-band"></div>

    <div class="person">
      <p class="person__name">ELLIOT MARSDEN</p>
      <p class="person__role">Managing Director</p>
    </div>

    <div class="address">
      <svg class="icon" viewBox="0 0 12 16" style="width:13px;height:17px"><path d="M6 0a6 6 0 0 0-6 6c0 4.5 6 10 6 10s6-5.5 6-10a6 6 0 0 0-6-6zm0 8.5A2.5 2.5 0 1 1 6 3.5a2.5 2.5 0 0 1 0 5z"/></svg>
      <p>061 12th floor.Park<br>Harbour Road BSN</p>
    </div>

    <ul class="contacts">
      <li><svg class="icon" viewBox="0 0 16 16"><path d="M3.5 1 6 4 4.6 5.8a9 9 0 0 0 5.6 5.6L12 10l3 2.5-1.6 2.3C7.5 15 1 8.5 1.2 2.6z"/></svg>012 555 0147</li>
      <li><svg class="icon" viewBox="0 0 16 16"><rect x="4" y="1" width="8" height="14" rx="1.5"/></svg>012 555 0147</li>
      <li><svg class="icon" viewBox="0 0 16 16"><rect x="1" y="5" width="14" height="8" rx="1"/><rect x="4" y="1" width="8" height="3"/></svg>012 555 0147</li>
      <li><svg class="icon" viewBox="0 0 16 16"><path d="M1 3h14v10H1zM2 4l6 5 6-5z"/></svg>yourname@mail.example</li>
      <li><svg class="icon" viewBox="0 0 16 16"><circle cx="8" cy="8" r="7"/></svg>www.yoursitename.example</li>
    </ul>
  </section>

</main>
</body>
</html>
```